Creative & Professional Business Card for hair salon

We are looking to update our business cards. Our salon is creative, modern, progressive and professional and looking for a design that will reflect this.

```html
<!DOCTYPE html>
<html lang="en">
<head>
<meta charset="utf-8">
<title>Silver Crest Studio – Business Card</title>
<link href="https://fonts.googleapis.com/css2?family=Great+Vibes&family=Open+Sans:wght@300;400;600&display=swap" rel="stylesheet">
<style>
  :root {
    --backdrop: #e4e2de;
    --paper: #f4f4f2;
    --ink: #27313d;
    --teal: #3c7782;
    --navy: #1b3a5c;
    --rule: #5b7f97;
    --brand: #3f6f86;
  }
  * { margin: 0; padding: 0; box-sizing: border-box; }
  html, body {
    width: 1200px; height: 1200px; overflow: hidden;
    background: var(--backdrop);
    font-family: "Open Sans", Arial, sans-serif;
    color: var(--ink);
  }
  .sheet {
    width: 1200px; height: 1200px;
    display: flex; flex-direction: column; align-items: center; justify-content: center;
    gap: 80px;
  }
  .card {
    position: relative;
    width: 840px; height: 480px;
    background: var(--paper);
    box-shadow: 0 2px 10px rgba(0,0,0,0.12);
    overflow: hidden;
  }

  /* Front */
  .holder-name {
    position: absolute; left: 60px; top: 40px;
    font-family: "Great Vibes", cursive;
    font-size: 58px; color: var(--brand); font-weight: 400;
  }
  .address {
    position: absolute; left: 62px; top: 122px;
    display: flex; align-items: center; gap: 12px;
    font-size: 21px;
  }
  .front-rule {
    position: absolute; left: 60px; top: 168px;
    width: 720px; height: 1.5px; background: var(--rule);
  }
  .contact-list {
    position: absolute; left: 62px; top: 190px;
    list-style: none; display: flex; flex-direction: column; gap: 6px;
    font-size: 21px;
  }
  .contact-list li { display: flex; align-items: center; gap: 12px; }
  .icon { width: 20px; height: 20px; flex: none; fill: var(--ink); }
  .brand-name {
    position: absolute;
    font-family: "Open Sans", Arial, sans-serif;
    font-weight: 300; color: var(--brand);
    display: flex; align-items: center; gap: 14px;
  }
  .brand-name .dot {
    width: 16px; height: 16px; border-radius: 50%; background: var(--brand);
  }
  .front .brand-name { right: 70px; top: 230px; font-size: 40px; }
  .social {
    position: absolute; right: 60px; bottom: 92px;
    display: flex; align-items: center; gap: 10px;
    font-size: 19px;
  }
  .social .square { width: 22px; height: 22px; background: var(--navy); border-radius: 3px; }
  .band-teal {
    position: absolute; left: 0; bottom: 0;
    width: 380px; height: 70px; background: var(--teal);
  }
  .band-navy {
    position: absolute; left: 395px; right: 0; bottom: 0;
    height: 70px; background: var(--navy);
  }

  /* Back */
  .back .brand-name { right: 80px; top: 110px; font-size: 44px; }
  .appointment-label {
    position: absolute; left: 110px; top: 230px;
    font-size: 26px; font-weight: 600; color: var(--navy);
  }
  .appointment-line {
    position: absolute; left: 110px; right: 90px; top: 350px;
    height: 2px; background: var(--rule);
  }
  .back .band-full {
    position: absolute; left: 0; right: 0; bottom: 0;
    height: 50px; background: var(--navy);
  }
</style>
</head>
<body>
<main class="sheet">

  <section class="card front" aria-label="Business card front">
    <h1 class="holder-name">Jo Merrin</h1>
    <p class="address">
      <svg class="icon" viewBox="0 0 24 24" aria-hidden="true"><path d="M12 2a7 7 0 0 0-7 7c0 5 7 13 7 13s7-8 7-13a7 7 0 0 0-7-7zm0 9.5A2.5 2.5 0 1 1 12 6.5a2.5 2.5 0 0 1 0 5z"/></svg>
      5/22 Harbour Lane, Eastvale
    </p>
    <div class="front-rule"></div>
    <ul class="contact-list">
      <li>
        <svg class="icon" viewBox="0 0 24 24" aria-hidden="true"><path d="M3 6c0-1.5 3-3 9-3s9 1.5 9 3v2h-5V6.5c-1-.4-2.4-.5-4-.5s-3 .1-4 .5V8H3zM6 10h12l2 9H4z"/></svg>
        07 5500 0199
      </li>
      <li>
        <svg class="icon" viewBox="0 0 24 24" aria-hidden="true"><circle cx="12" cy="12" r="9" fill="none" stroke="currentColor" stroke-width="2" style="stroke:#27313d"/><path d="M3 12h18M12 3c3 3 3 15 0 18M12 3c-3 3-3 15 0 18" fill="none" stroke="#27313d" stroke-width="1.6"/></svg>
        www.silvercreststudio.com.au
      </li>
      <li>
        <svg class="icon" viewBox="0 0 24 24" aria-hidden="true"><path d="M2 5h20v14H2zm2 2v.5l8 5.5 8-5.5V7z"/></svg>
        Salon@silvercreststudio.com.au
      </li>
    </ul>
    <div class="brand-name"><span class="dot"></span>Silver Crest Studio</div>
    <p class="social">/SilverCrestStudiobyJoMerrin <span class="square"></span></p>
    <div class="band-teal"></div>
    <div class="band-navy"></div>
  </section>

  <section class="card back" aria-label="Business card back">
    <div class="brand-name"><span class="dot"></span>Silver Crest Studio</div>
    <p class="appointment-label">Your Next Appointment Is</p>
    <div class="appointment-line"></div>
    <div class="band-full"></div>
  </section>

</main>
</body>
</html>
```